Welcome E-Mail Design - UI/UX Designer

Hello All,

We are in the process of redesigning our complete webpage http://lnk.example-short.net/7QpTmR4.
While this, we are also looking to redesign our E-Mails.
The winner of the contest will be able to take the design of remaining E-Mail (more than 5)

I'm looking for an expert to work on Welcome E-Mail Design at the first place. If work delivery is as we expect, we would then assign the expert with other remaining E-Mails.

Here the text of welcome mail:
-------
Hi xxx,

We make it our mission to provide a reliable and safe gateway for services from Africa to the world.

Since we started in 2016, thousands of users have joined us on our journey to support our lovely continent.

We are happy to have you as our newest member:

Your User ID is <User's E-MAIL>

To fully activate your account, <a href="user's activation URL">login and follow the steps on the page </a>.

For any questions contact our Customer Care team at support@velunor-hq.com.

Best,
The team

---------

You can check in attachment our new design, which is not yet online.
Waiting for your proposal

Thanks in advance.

```html
<!DOCTYPE html>
<html lang="en">
<head>
<meta charset="utf-8">
<title>Welcome to velunor</title>
<link rel="stylesheet" href="https://fonts.googleapis.com/css2?family=Arimo:wght@400;700&family=Tinos&display=swap">
<style>
  :root {
    --page-bg: #ffffff;
    --band-bg: #d9dbf3;
    --card-bg: #fdfbfb;
    --ink: #222222;
    --ink-soft: #333333;
    --accent-red: #ee1111;
    --accent-orange: #fbab32;
    --brand: #1f1f1f;
    --art-blue: #c9d6fb;
    --social: #e7e7ef;
    --social-ring: #c9cbe0;
  }
  * { box-sizing: border-box; margin: 0; padding: 0; }
  html, body { width: 710px; height: 1200px; overflow: hidden; background: var(--page-bg); }
  body { position: relative; font-family: "Arimo", Arial, sans-serif; color: var(--ink-soft); }

  .mail-band {
    position: absolute; left: 22px; top: 57px; width: 667px; height: 1059px;
    background: var(--band-bg);
  }
  .brand {
    position: absolute; left: 0; width: 100%; text-align: center;
    font-family: "Arimo", Arial, sans-serif; font-weight: 700; color: var(--brand);
  }
  .brand--header { top: 17px; font-size: 34px; letter-spacing: 0.5px; }
  .brand--footer { top: 930px; font-size: 24px; }

  .mail-card {
    position: absolute; left: 58px; top: 81px; width: 550px; height: 832px;
    background: var(--card-bg);
    box-shadow: 0 1px 4px rgba(60, 60, 110, 0.25);
  }
  .hero-art {
    position: absolute; left: 119px; top: 40px; width: 311px; height: 154px;
    background: radial-gradient(circle at 50% 45%, var(--art-blue) 0%, #e4eafc 55%, #f7f8fe 100%);
    border-radius: 4px;
  }
  .greeting {
    position: absolute; top: 233px; left: 0; width: 100%; text-align: center;
    font-size: 24px; font-weight: 700; color: var(--accent-red);
  }
  .headline {
    position: absolute; top: 262px; left: 0; width: 100%; text-align: center;
    font-size: 30px; font-weight: 700; color: var(--ink);
  }
  .copy { position: absolute; left: 24px; width: 500px; font-size: 11.2px; line-height: 1.2; }
  .copy--lead { top: 335px; font-size: 12.6px; font-weight: 700; color: var(--ink-soft); line-height: 1.15; }
  .copy--since { top: 379px; }
  .copy--member { top: 422px; }
  .copy--activate { top: 546px; }
  .copy--minutes { top: 648px; }
  .copy--contact { top: 690px; }
  .copy--sign { top: 719px; }
  .copy--team { top: 748px; }

  .user-id-box {
    position: absolute; left: 149px; top: 451px; width: 251px; height: 82px;
    background: var(--accent-orange); border-radius: 7px;
    text-align: center; font-size: 11.2px; color: var(--ink-soft); padding-top: 15px;
  }
  .user-id-box .user-id { color: var(--accent-red); font-weight: 700; }
  .user-id-box .note { margin-top: 16px; }

  .action-button {
    position: absolute; left: 141px; top: 576px; width: 267px; height: 44px;
    background: var(--accent-orange); border-radius: 7px;
    display: flex; align-items: center; justify-content: center;
    font-size: 11.5px; color: var(--ink-soft); text-decoration: none;
  }

  .copyright {
    position: absolute; top: 972px; left: 0; width: 100%; text-align: center;
    font-family: "Tinos", "Times New Roman", serif; font-size: 12px; color: var(--ink);
  }
  .social-row {
    position: absolute; top: 1000px; left: 0; width: 100%;
    display: flex; justify-content: center; gap: 6px;
  }
  .social-dot {
    width: 21px; height: 21px; border-radius: 50%;
    background: var(--social); border: 2px solid var(--social-ring);
  }
</style>
</head>
<body>
  <div class="mail-band">
    <div class="brand brand--header">velunor</div>

    <main class="mail-card">
      <div class="hero-art" role="img" aria-label="Illustration of two people with phones celebrating a money transfer, coins and chat bubbles around them"></div>

      <p class="greeting">Hello John!</p>
      <h1 class="headline">Thank You For Choosing Us</h1>

      <p class="copy copy--lead">We make it our mission to provide a reliable and safe gateway for services from Africa to the world.</p>
      <p class="copy copy--since">Since we started in 2016, thousands of users have joined us on our journey to support our lovely continent.</p>
      <p class="copy copy--member">We are happy to have you as our newest member:</p>

      <div class="user-id-box">
        <p>Your User ID is <span class="user-id">john@inboxmail.net</span></p>
        <p class="note">This Id functions as your user name</p>
      </div>

      <p class="copy copy--activate">To fully activate your account:</p>
      <a class="action-button" href="#">Login And Follow The Steps On The Page</a>

      <p class="copy copy--minutes">It shouldn't take more than a few minutes to fully activate your account. Then you will be able to deposite funds and start send money to your loved ones</p>
      <p class="copy copy--contact">For any questions contact our Customer Care team at support@velunor-hq.com.</p>
      <p class="copy copy--sign">Best,</p>
      <p class="copy copy--team">The Team.</p>
    </main>

    <div class="brand brand--footer">velunor</div>
    <p class="copyright">copyright velunor 2019. All right reserved</p>
    <nav class="social-row" aria-label="Social links">
      <span class="social-dot"></span>
      <span class="social-dot"></span>
      <span class="social-dot"></span>
      <span class="social-dot"></span>
      <span class="social-dot"></span>
    </nav>
  </div>
</body>
</html>
```